Design the Mobile Version of Existing Web Based Health Platform

Loomcrest is a social business enterprise that focus on public health by applying innovative healthcare services and consumer internet technology. Loomcrest offers a personalized platform of health promotion and disease prevention that puts the individual back in control of his life.

Loomcrest is looking for a Mobile Web UX/Visual Design professional to create a mobile version of Loomcrest website platform for iPhone, iPad/tablet and Android.

Contestants must to check www.loomcrest-demo.com.br to have a better understanding of Loomcrest Platform by creating an account (it's in portuguese, but anyone can get the general idea).

The mobile version of Loomcrest should have very similar functionality and user flows. This job is not to reengineer or re-imagine Loomcrest. It is just to reformat the existing functionality so it works well on mobile devices.

This description below is to help you to understand the core features of the platform (check the attachments to see the new web design of each one):

- Personally Controlled Health Record - PCHR enables an individual to own and manage a complete, secure, digital copy of her health and wellness information.
- Health Risk Assessments - is a process to estimate the nature and probability of adverse health effects, based on personal and family historical data, behavior and environment.
- Simulation of future health - "what if analysis" that emphasizes health education and behavior change.
- Step Quests - a program that gives you the opportunity to the participant to advance his personal well-being by doing simple Step Quests
- Health Alerts and Recommendations and Missing Data - Recommendations based on Wellbeing Bureau Guidelines and Federal Wellness Review Panel (FWRP), plus notifications to update outdated information.

The deliverable for this project is a psd file with a designed mobile version of Loomcrest.

A new design of the web platform is under construction. You can also check it looking at the files attached.

Target Market(s)

people 25-40 years old, 60% female, socially engaged

Industry/Entity Type

Healthcare

Requirements
Must have
• iPhone, iPad and Android version

Design must cover all current functionalities available on the web version (please, ensure you understand all features by creating an account at www.loomcrest-demo.com.br)

- Login/Sign up
- Welcome (first assessment)
- Add to Personal Controlled Health Record (PCHR)
- Update/Remove PCHR
- List PCHR
- Riskgrid (risk assessmen results)
- Simulation
- Alerts
- Missing data
- Recommendations
- StepQuest
- Badges
- Configurations

It's important to check the attachments to see how the web platform design is evolving.

```html
<!DOCTYPE html>
<html lang="pt">
<head>
<meta charset="utf-8">
<title>Loomcrest – Registre-se</title>
<link rel="stylesheet" href="https://fonts.googleapis.com/css2?family=Open+Sans:wght@400;600;700&display=swap">
<style>
  :root {
    --band-bg: #e3ecf6;
    --page-bg: #ffffff;
    --brand-orange: #f5922b;
    --brand-orange-deep: #f26a3a;
    --title-navy: #2f3f73;
    --field-bg: #eaeff6;
    --field-border: #cfd6e0;
    --placeholder: #9aa3ae;
    --muted: #9ba1a8;
    --link-blue: #1f7fc4;
    --white: #ffffff;
  }
  * { box-sizing: border-box; margin: 0; padding: 0; }
  html, body { width: 800px; height: 1200px; overflow: hidden; }
  body {
    font-family: "Open Sans", Arial, sans-serif;
    background: var(--page-bg);
    position: relative;
  }
  .hero-band {
    position: absolute; left: 0; top: 0; width: 800px; height: 516px;
    background: radial-gradient(ellipse at 50% 90%, #e8eff8 0%, var(--band-bg) 60%);
    border-bottom: 1px solid #d8dee6;
  }
  .hero-fade {
    position: absolute; left: 0; top: 517px; width: 800px; height: 84px;
    background: linear-gradient(#f1f2f4, var(--page-bg));
  }
  .brand {
    position: absolute; left: 0; top: 340px; width: 800px; height: 60px;
    display: flex; align-items: center; justify-content: center; gap: 16px;
  }
  .brand-square {
    width: 40px; height: 40px;
    background: var(--brand-orange);
  }
  .brand-name {
    font-weight: 400; font-size: 44px; line-height: 1;
    color: var(--title-navy);
  }
  .signup {
    position: absolute; left: 211px; top: 596px; width: 378px;
  }
  .signup-title {
    text-align: center; font-size: 18px; font-weight: 400;
    color: var(--title-navy); margin-bottom: 16px;
  }
  .field {
    display: block; width: 100%; height: 36px; margin-bottom: 13px;
    background: var(--field-bg); border: 1px solid var(--field-border);
    padding: 0 19px; font: 400 13px "Open Sans", Arial, sans-serif;
    color: #333;
  }
  .field::placeholder { color: var(--placeholder); }
  .terms {
    display: flex; align-items: center; gap: 10px;
    font-size: 11.5px; color: var(--muted); margin-top: 3px;
  }
  .terms-box {
    width: 21px; height: 21px; border: 1px solid var(--field-border);
    background: var(--white); appearance: none;
  }
  .terms a { color: var(--link-blue); text-decoration: none; font-weight: 600; }
  .submit {
    display: block; width: 100%; height: 42px; margin-top: 12px;
    background: var(--brand-orange); border: 0; color: var(--white);
    font: 700 13px "Open Sans", Arial, sans-serif; letter-spacing: 0.3px;
  }
  .help-button {
    position: absolute; left: 693px; top: 1115px; width: 50px; height: 44px;
    border-radius: 4px;
    background: linear-gradient(90deg, var(--brand-orange), var(--brand-orange-deep));
    color: var(--white); font-size: 34px; font-weight: 700;
    display: flex; align-items: center; justify-content: center; line-height: 1;
  }
</style>
</head>
<body>
  <header class="hero-band"></header>
  <div class="hero-fade"></div>

  <div class="brand">
    <div class="brand-square"></div>
    <div class="brand-name">Loomcrest</div>
  </div>

  <form class="signup">
    <h1 class="signup-title">Registre-se Loomcrest</h1>
    <input class="field" type="email" placeholder="Email address...">
    <input class="field" type="password" placeholder="Password...">
    <input class="field" type="password" placeholder="Rewrite Password...">
    <label class="terms">
      <input class="terms-box" type="checkbox">
      <span>I accept the <a href="#">Terms and Conditions</a></span>
    </label>
    <button class="submit" type="button">SIGN IN</button>
  </form>

  <div class="help-button" aria-label="Help">?</div>
</body>
</html>
```